Civil engineering company | Billboard

We need a billboard design for Velmora- civil engineering company. We want big logo in the center of billboard and web site (www.velmora.hr) below the logo. Also, we want an subtle abstract pattern in the background. Dimensions of the billboard are: width :10 m, height: 2m. Design must be celan and modern.
Industry/Entity Type
Civil engineering
Font styles to use
Sans Serif
Colors
F0912C
F2A743
F7CA91
FBE8D2
FDF5EE
Requirements
Must have
- Logo and new unique pattern design for Velomra company
Should not have
- pictures of construction machinery and tools

```html
<!DOCTYPE html>
<html lang="hr">
<head>
<meta charset="utf-8">
<title>Velmora – billboard</title>
<link rel="stylesheet" href="https://fonts.googleapis.com/css2?family=Poppins:wght@300;500;600&display=swap">
<style>
  :root {
    --canvas-bg: #d9d9d9;
    --panel-white: #ffffff;
    --brand-orange: #e8892f;
    --band-grey: #3f3f3f;
    --text-grey: #4a4a4a;
    --sunset-dark: #141009;
    --sunset-amber: #f0a23a;
    --sunset-gold: #f7c85a;
    --sky-blue: #6f9fc4;
    --sky-pale: #a9c8dc;
    --site-dark: #17181c;
  }
  * { margin: 0; padding: 0; box-sizing: border-box; }
  html, body {
    width: 960px;
    height: 1200px;
    overflow: hidden;
    background: var(--canvas-bg);
  }
  .canvas {
    position: relative;
    width: 960px;
    height: 1200px;
  }
  .billboard {
    position: absolute;
    left: 40px;
    top: 512px;
    width: 880px;
    height: 176px;
    display: block;
    box-shadow: 0 2px 6px rgba(0,0,0,0.18);
  }
  .brand-name {
    font-family: "Poppins", sans-serif;
    font-weight: 500;
    fill: var(--brand-orange);
    letter-spacing: 2px;
  }
  .tagline {
    font-family: "Poppins", sans-serif;
    font-weight: 500;
    fill: var(--text-grey);
    letter-spacing: 0.3px;
  }
  .web-address {
    font-family: "Poppins", sans-serif;
    font-weight: 300;
    fill: var(--panel-white);
    letter-spacing: 9px;
  }
  .web-address .web-domain { font-weight: 600; }
</style>
</head>
<body>
<main class="canvas">
  <svg class="billboard" viewBox="0 0 1457 291" xmlns="http://www.w3.org/2000/svg">
    <defs>
      <linearGradient id="sunset-sky" x1="0" y1="0" x2="1" y2="1">
        <stop offset="0" stop-color="var(--sunset-dark)"/>
        <stop offset="0.35" stop-color="var(--sunset-amber)"/>
        <stop offset="0.65" stop-color="var(--sunset-gold)"/>
        <stop offset="1" stop-color="var(--sunset-dark)"/>
      </linearGradient>
      <linearGradient id="blue-sky" x1="0" y1="0" x2="0" y2="1">
        <stop offset="0" stop-color="var(--sky-blue)"/>
        <stop offset="0.55" stop-color="var(--sky-pale)"/>
        <stop offset="1" stop-color="var(--site-dark)"/>
      </linearGradient>
    </defs>

    <rect class="center-panel" x="0" y="0" width="1457" height="291" fill="var(--panel-white)"/>

    <polygon class="photo photo-left" role="img"
      aria-label="Silhouettes of engineers on a building site at sunset with a tower crane"
      points="0,0 411,0 466,145 411,291 0,291" fill="url(#sunset-sky)"/>
    <polygon class="photo photo-right" role="img"
      aria-label="Workers on scaffolding under a blue evening sky"
      points="1046,0 1457,0 1457,291 1046,291 991,145" fill="url(#blue-sky)"/>

    <g class="accent-triangles" fill="var(--brand-orange)">
      <polygon points="421,0 490,0 452,76"/>
      <polygon points="421,291 490,291 452,215"/>
      <polygon points="967,0 1036,0 1005,76"/>
      <polygon points="967,291 1036,291 1005,215"/>
    </g>

    <text class="brand-name" x="728" y="140" text-anchor="middle" font-size="64">VELMORA</text>
    <text class="tagline" x="728" y="182" text-anchor="middle" font-size="13">IZVOĐENJE I VOĐENJE GRAĐEVINSKIH RADOVA</text>

    <polygon class="web-band" points="466,222 991,222 961,291 496,291" fill="var(--band-grey)"/>
    <text class="web-address" x="728" y="268" text-anchor="middle" font-size="30">www.<tspan class="web-domain">velmora</tspan>.hr</text>
  </svg>
</main>
</body>
</html>
```